Etiketten für Kuchen im Glas
Zielgruppe
Die Firma Brelkat bietet kulinarische Präsente und Geschenkideen zum Thema kreatives Backen an. Unsere Zielgruppe ist B2C und Werbetreibende, die unsere Produkte als Geschenke einsetzen.
Aufgabenstellung
Für unsere Zielgruppe "Feinkostläden" benötigen wir ein etwas edleres klasssisches Etiketten-Design.
Gestaltet wird der Deckel und die Vorderseite eines Etiketts für ein 290 ml FUMS-Glas. Die entsprechende Designvorlage steht hier zum Download bereit:
https://files.tralvex-speicher.de/u/4827351/7902_01358_0000-Vorlage%20CMYK%20v08_2013-09.psd
Benötigt werden 4 unterschiedliche Etiketten, die aber aus einem "Guss" sein sollten für die Sorten: Stracciatella, Schokolade, Zitrone, Stollen. Die Sorte sollte mit auf dem Etikett stehen.
Sonstige Angaben auf dem Etikett:
- optional "Kuchen im Glas"
- gerne Grünhof Logo (siehe Anhang)
- optional "fertig gebacken". Könnte z.B. gut auf dem Deckel in Kombination mit "Kuchen im Gla" stehen
Achtung: Das Etikett für die Rückseite mit Deklaration muss nicht gestaltet werden.
Tipps: Das Etikett ist konisch und das Glas rund. Das bedeutet, dass Bilder + Schriften mit einer leichten Wölbung kreiert werden sollten. Für die Wölbung kann man sich gut an der unteren Designlinie orientieren.
Farbgestaltung: eher dunkel; z.B. Grau, Dunkelblau evtl. Schwarz
Schriften: Es dürfen auch kostenpflichtige Schriften verwendet werden. Freie Schriften allerdings bevorzugt
Format: Photoshop PSD inklusive allen Ebenen und verwendeten Elementen als einzelne Ebene.
Bei Fragen gerne melden, ich freue mich auf Eure Designs.

```html
<!DOCTYPE html>
<html lang="de">
<head>
<meta charset="utf-8">
<title>Kuchen im Glas – Stollen Etiketten</title>
<link rel="stylesheet" href="https://fonts.googleapis.com/css2?family=Great+Vibes&family=EB+Garamond:ital,wght@0,600;1,400&display=swap">
<style>
  :root {
    --paper: #ffffff;
    --label-dark: #1c1a19;
    --label-mid: #2e2926;
    --rim-copper: #9c3a14;
    --script-white: #ffffff;
    --gold: #c9a371;
    --cake-light: #b08a62;
    --cake-dark: #6b4a2f;
    --seal-green: #4a8a4a;
  }
  html, body {
    margin: 0;
    width: 1118px;
    height: 1200px;
    overflow: hidden;
    background: var(--paper);
  }
  .sheet { display: block; width: 1118px; height: 1200px; }
  .variety { font-family: "Great Vibes", cursive; fill: var(--gold); }
  .title-script { font-family: "Great Vibes", cursive; fill: var(--script-white); }
  .tagline { font-family: "EB Garamond", Georgia, serif; font-style: italic; fill: var(--script-white); }
  .brand-name { font-family: "EB Garamond", Georgia, serif; font-weight: 600; fill: var(--script-white); }
  .rim { fill: none; stroke: var(--rim-copper); stroke-width: 5; }
</style>
</head>
<body>
<svg class="sheet" viewBox="0 0 1118 1200" xmlns="http://www.w3.org/2000/svg">
  <defs>
    <radialGradient id="ornament-tone" cx="50%" cy="45%" r="60%">
      <stop offset="0" stop-color="var(--label-mid)"/>
      <stop offset="1" stop-color="var(--label-dark)"/>
    </radialGradient>
    <linearGradient id="cake-tone" x1="0" y1="0" x2="1" y2="1">
      <stop offset="0" stop-color="var(--cake-light)"/>
      <stop offset="1" stop-color="var(--cake-dark)"/>
    </linearGradient>
  </defs>

  <!-- Deckel-Etikett -->
  <g class="lid-label">
    <circle cx="557" cy="312" r="251" fill="var(--label-dark)"/>
    <circle cx="557" cy="312" r="236" fill="url(#ornament-tone)" role="img" aria-label="Dezentes Schnörkel-Ornament als Hintergrund"/>
    <circle class="rim" cx="557" cy="312" r="237"/>

    <text class="variety" x="553" y="170" font-size="36" text-anchor="middle">-Stollen-</text>
    <text class="title-script" x="356" y="272" font-size="104">Kuchen</text>
    <text class="title-script" x="510" y="314" font-size="62">im</text>
    <text class="title-script" x="574" y="318" font-size="108">Glas</text>
    <text class="tagline" x="380" y="314" font-size="24">… fertig</text>
    <text class="tagline" x="401" y="338" font-size="24">gebacken.</text>

    <path role="img" aria-label="Foto: drei Scheiben Christstollen mit Rosinen und Puderzucker"
      fill="url(#cake-tone)"
      d="M385,412 Q430,372 500,368 Q540,345 590,342 Q620,330 650,338 Q690,370 698,420 Q700,455 672,482 L640,500 Q600,505 560,525 Q520,536 470,512 Q410,470 385,412 Z"/>
  </g>

  <!-- Vorderseiten-Etikett (konisch) -->
  <g class="front-label">
    <path fill="var(--label-dark)"
      d="M78,707 Q557,616 1036,707 Q1057,704 1055,726 L990,1110 Q986,1132 965,1129 Q557,1005 148,1129 Q127,1132 123,1110 L59,727 Q57,709 78,707 Z"/>
    <path fill="url(#ornament-tone)" role="img" aria-label="Dezentes Schnörkel-Ornament als Hintergrund"
      d="M82,735 Q557,639 1032,735 L970,1105 Q557,991 145,1105 Z"/>
    <path class="rim" d="M82,735 Q557,639 1032,735 L970,1105 Q557,991 145,1105 Z"/>

    <text class="variety" x="557" y="748" font-size="36" text-anchor="middle">-Stollen-</text>
    <text class="title-script" x="292" y="838" font-size="110" transform="rotate(-4 292 838)">Kuchen</text>
    <text class="title-script" x="508" y="878" font-size="64">im</text>
    <text class="title-script" x="590" y="882" font-size="112" transform="rotate(8 590 882)">Glas</text>
    <text class="tagline" x="316" y="902" font-size="24" transform="rotate(-10 316 902)">… fertig gebacken.</text>

    <g class="brand-mark">
      <rect x="842" y="733" width="16" height="16" fill="var(--seal-green)"/>
      <text class="brand-name" x="864" y="748" font-size="24">Grünhof</text>
    </g>

    <path role="img" aria-label="Foto: drei Scheiben Christstollen mit Rosinen und Puderzucker"
      fill="url(#cake-tone)"
      d="M358,985 Q400,945 470,935 Q510,915 560,910 Q600,895 640,902 Q690,930 702,985 Q706,1025 690,1058 Q620,1062 560,1066 Q470,1068 400,1050 Q365,1020 358,985 Z"/>
  </g>
</svg>
</body>
</html>
```